Mouthguard Marketing

We specialise in the production of custom made mouthguards for sportsmen and women. These are made by direct public contact or via Dental Surgeons. On our postcard we would need the following...
*Custom made sports guards from £20 (Boxed)
Bleaching trays from £28 (pair) (Boxed)
Orthodontic retainers £28 (pair)
All the above manufactured from advanced pressure and vacuum forming techniques.
Please contact Tom or Owen (01482) 357261 Maple Dental Laboratory Ltd

Industry/Entity Type

Dental

```html
<!DOCTYPE html>
<html lang="en">
<head>
<meta charset="utf-8">
<title>Custom Made Mouthguards – Postcard</title>
<link href="https://fonts.googleapis.com/css2?family=Open+Sans:ital,wght@0,300;0,400;0,600;0,700;1,400&family=Oswald:wght@500;600;700&display=swap" rel="stylesheet">
<style>
  :root{
    --sky:#2aa6e0;
    --sky-deep:#0a72bb;
    --navy:#0d3566;
    --navy-deep:#082a52;
    --ink:#14375e;
    --ink-dark:#12324f;
    --note-ink:#123a66;
    --accent-red:#c8102e;
    --title-blue:#2a98d4;
    --card-blue:#1d9bd7;
    --white:#ffffff;
    --page:#ffffff;
  }
  *{box-sizing:border-box;margin:0;padding:0}
  html,body{width:787px;height:1200px;overflow:hidden;background:var(--page)}
  body{position:relative;font-family:"Open Sans",Arial,sans-serif}
  .card{position:absolute;width:750px;overflow:hidden;background:var(--white);box-shadow:0 2px 6px rgba(0,0,0,.35)}
  .card--front{left:35px;top:33px;height:579px}
  .card--back{left:35px;top:640px;height:555px}
  .layer{position:absolute;left:0;top:0}
  .abs{position:absolute}
  .price{color:var(--white);font-family:"Oswald",Arial,sans-serif;font-weight:600;font-size:18px;line-height:26px;text-transform:uppercase;letter-spacing:.2px}
  .price small{display:block;font-family:"Open Sans",Arial,sans-serif;font-size:15px;line-height:26px;text-transform:none;font-weight:700}
  .process-note{left:92px;top:112px;color:var(--note-ink);font-style:italic;font-size:13.5px;white-space:nowrap}
  .title-light{font-weight:300;text-transform:uppercase;white-space:nowrap}
  .title-bold{font-family:"Oswald",Arial,sans-serif;font-weight:700;text-transform:uppercase;white-space:nowrap}
  .tagline{font-style:italic;white-space:nowrap}
  .contact{color:var(--white);text-align:center;white-space:nowrap}
  .contact__lead{font-style:italic}
  .contact__company,.contact__phone{font-family:"Oswald",Arial,sans-serif;font-weight:600}
  .contact__phone{display:flex;align-items:center;justify-content:center;gap:8px}
  .colour-note{font-family:"Oswald",Arial,sans-serif;font-weight:600;color:var(--ink-dark);font-size:13px;line-height:24px;text-transform:uppercase;white-space:nowrap}
  .colour-note .cap{font-size:17px}
  .partner-name{color:var(--white);font-size:11px;font-weight:600;white-space:nowrap}
  .swatch-grid{position:absolute;left:14px;top:222px;display:grid;grid-template-columns:66px 66px;column-gap:6px;row-gap:17px}
  .swatch{width:66px;height:28px;border-radius:14px 14px 10px 10px;box-shadow:0 2px 3px rgba(0,0,0,.25)}
</style>
</head>
<body>

<section class="card card--front">
  <svg class="layer" width="750" height="579" viewBox="0 0 750 579" aria-hidden="true">
    <defs>
      <linearGradient id="topBand" x1="0" y1="0" x2="1" y2="0">
        <stop offset="0" stop-color="#33addf"/>
        <stop offset="1" stop-color="#0b74bd"/>
      </linearGradient>
      <linearGradient id="baseBand" x1="0" y1="0" x2="0" y2="1">
        <stop offset="0" stop-color="#1c5b9c"/>
        <stop offset="1" stop-color="#082a52"/>
      </linearGradient>
    </defs>
    <polygon points="0,0 750,0 750,134 0,166" fill="url(#topBand)"/>
    <polygon points="0,166 750,134 750,140 0,172" fill="#8fcff0"/>
  </svg>

  <svg class="layer" width="750" height="579" viewBox="0 0 750 579" role="img" aria-label="Photo of a laughing ice hockey player in helmet and red glove, with a missing front tooth">
    <defs>
      <linearGradient id="playerPhoto" x1="0" y1="0" x2="1" y2="0">
        <stop offset="0" stop-color="#c9c3c0"/>
        <stop offset=".45" stop-color="#b0504a"/>
        <stop offset=".75" stop-color="#d2a58f"/>
        <stop offset="1" stop-color="#5a5a5c"/>
      </linearGradient>
    </defs>
    <polygon points="280,160 750,140 750,420 280,395" fill="url(#playerPhoto)"/>
  </svg>

  <svg class="layer" width="750" height="579" viewBox="0 0 750 579" aria-hidden="true">
    <polygon points="0,380 750,420 750,579 0,579" fill="url(#baseBand)"/>
  </svg>

  <svg class="abs" style="left:20px;top:300px" width="215" height="262" viewBox="0 0 215 262" role="img" aria-label="Photo of assorted coloured mouthguards resting on a white dental model">
    <defs>
      <linearGradient id="guardsPhoto" x1="0" y1="0" x2="0" y2="1">
        <stop offset="0" stop-color="#c6d7e6"/>
        <stop offset=".5" stop-color="#e8ecef"/>
        <stop offset="1" stop-color="#aebfcf"/>
      </linearGradient>
    </defs>
    <rect width="215" height="262" rx="30" fill="url(#guardsPhoto)"/>
  </svg>

  <div class="abs price" style="left:92px;top:28px">Custom made<br>sports guards<small>from £20 (Boxed)</small></div>
  <div class="abs price" style="left:299px;top:30px">Bleaching trays<small>from £28 per pair<br>(Boxed)</small></div>
  <div class="abs price" style="left:508px;top:28px">Orthodontic<br>retainers<small>£28 per pair</small></div>
  <p class="abs process-note">All manufactured from advanced pressure and vacuum forming techniques.</p>

  <h1 class="abs title-light" style="left:42px;top:184px;font-size:31px;color:var(--title-blue)">Custom Made</h1>
  <h2 class="abs title-bold" style="left:42px;top:220px;font-size:37px;color:var(--ink);letter-spacing:-.5px">Mouthguards</h2>
  <p class="abs tagline" style="left:42px;top:274px;font-size:19px;color:var(--accent-red)">for sports men &amp; women</p>

  <div class="abs contact" style="left:215px;top:429px;width:340px">
    <p class="contact__lead" style="font-size:17px">Please contact Tom or Owen</p>
    <p class="contact__company" style="font-size:24px;line-height:34px">Maple Dental Laboratory Ltd</p>
    <p class="contact__phone" style="font-size:30px;line-height:40px">
      <svg width="24" height="24" viewBox="0 0 24 24" aria-hidden="true"><circle cx="12" cy="12" r="10.5" fill="none" stroke="#fff" stroke-width="1.6"/><path d="M8 7.5c-.6 3.5 2.4 8 6.5 9l1.5-1.6-2-1.4-1 .8c-1.5-.7-2.7-2.2-3-3.8l1-.7-.9-2.2z" fill="#fff"/></svg>
      (01482) 357261
    </p>
  </div>

  <svg class="abs" style="left:556px;top:420px" width="90" height="90" viewBox="0 0 90 90" aria-hidden="true">
    <circle cx="45" cy="45" r="42" fill="none" stroke="#c9d6e6" stroke-width="2"/>
  </svg>
  <div class="abs" style="left:596px;top:530px;display:flex;align-items:center;gap:6px">
    <span style="display:inline-block;width:10px;height:10px;background:var(--white)"></span>
    <span class="partner-name">Maple Standard Dental</span>
  </div>
</section>

<section class="card card--back">
  <svg class="layer" width="750" height="555" viewBox="0 0 750 555" aria-hidden="true">
    <polygon points="0,0 410,0 330,555 0,555" fill="var(--card-blue)"/>
  </svg>

  <svg class="abs" style="left:15px;top:0" width="152" height="216" viewBox="0 0 152 216" role="img" aria-label="Photo of a smiling skier in helmet and goggles holding a pink mouthguard">
    <defs>
      <linearGradient id="skierPhoto" x1="0" y1="0" x2="0" y2="1">
        <stop offset="0" stop-color="#9fc4d8"/>
        <stop offset=".5" stop-color="#d9b7a0"/>
        <stop offset="1" stop-color="#eef1f4"/>
      </linearGradient>
    </defs>
    <rect x="1.5" y="1.5" width="149" height="213" fill="url(#skierPhoto)" stroke="#9fd3ee" stroke-width="3"/>
  </svg>

  <div class="swatch-grid">
    <div class="swatch" style="background:#6a2a86" role="img" aria-label="Photo of a purple and white striped mouthguard"></div>
    <div class="swatch" style="background:#b2334a" role="img" aria-label="Photo of a stars and stripes mouthguard"></div>
    <div class="swatch" style="background:#7a1f2e" role="img" aria-label="Photo of a maroon and yellow mouthguard"></div>
    <div class="swatch" style="background:#1b1b1d" role="img" aria-label="Photo of a black and white fang mouthguard"></div>
    <div class="swatch" style="background:#5e3a7a" role="img" aria-label="Photo of a purple, green and red mouthguard"></div>
    <div class="swatch" style="background:#d9d9d9" role="img" aria-label="Photo of a white and black striped mouthguard"></div>
    <div class="swatch" style="background:#d42a2a" role="img" aria-label="Photo of a red and white mouthguard"></div>
    <div class="swatch" style="background:#c81f26" role="img" aria-label="Photo of a red flag design mouthguard"></div>
    <div class="swatch" style="background:#8fb124" role="img" aria-label="Photo of a green and yellow mouthguard"></div>
    <div class="swatch" style="background:#24306e" role="img" aria-label="Photo of a union flag design mouthguard"></div>
  </div>

  <svg class="abs" style="left:172px;top:312px" width="170" height="110" viewBox="0 0 170 110" role="img" aria-label="Photo of a purple glitter mouthguard on a turquoise storage case">
    <defs>
      <linearGradient id="caseGuardPhoto" x1="0" y1="0" x2="1" y2="1">
        <stop offset="0" stop-color="#6fd3d6"/>
        <stop offset=".6" stop-color="#9a5bc0"/>
        <stop offset="1" stop-color="#7a3fa3"/>
      </linearGradient>
    </defs>
    <rect width="170" height="110" rx="30" fill="url(#caseGuardPhoto)" opacity=".85"/>
  </svg>

  <h1 class="abs title-light" style="left:188px;top:38px;font-size:25px;color:var(--ink-dark)">Custom Made</h1>
  <h2 class="abs title-bold" style="left:188px;top:70px;font-size:28px;color:var(--ink-dark);letter-spacing:-.4px">Mouthguards</h2>
  <p class="abs tagline" style="left:188px;top:111px;font-size:14px;color:var(--ink-dark)">for sports men &amp; women</p>

  <p class="abs colour-note" style="left:210px;top:154px"><span class="cap">I</span>n a choice of <span class="cap">26</span><br>vibrant colours<br>including clear</p>

  <div class="abs contact" style="left:86px;top:436px;text-align:left">
    <p class="contact__lead" style="font-size:14px">Please contact Tom or Owen</p>
    <p class="contact__company" style="font-size:19px;line-height:27px">Maple Dental Laboratory Ltd</p>
    <p class="contact__phone" style="font-size:25px;line-height:34px;justify-content:flex-start">
      <svg width="21" height="21" viewBox="0 0 24 24" aria-hidden="true"><circle cx="12" cy="12" r="10.5" fill="none" stroke="#fff" stroke-width="1.6"/><path d="M8 7.5c-.6 3.5 2.4 8 6.5 9l1.5-1.6-2-1.4-1 .8c-1.5-.7-2.7-2.2-3-3.8l1-.7-.9-2.2z" fill="#fff"/></svg>
      (01482) 357261
    </p>
  </div>
</section>

</body>
</html>
```